GRAVELDUST: Chapters Of A Winter

I need some artwork created for my album cover. The concept or theme of the album is hard luck. To have bad luck. But not to focus solely on dice, cats, or unlucky symbols but I wouldn't mind seeing the incorporation of symbols or images that are supposed to be lucky like clovers dice, etc. I grew up in Chicago in the 90's, military after that, then got into trouble. Ten years later, I have kids, wife, etc....Hope this helps I can include link to visit page to hear music if it helps.

https://www.tunekettle.com/vodrani

So whatever you can come up with I'm sure will be amazing. I'm not sure if I even like half the images I uploaded but its something. The drawings are for my graveldust logo. Thanks for all your help and hard work in advance.

Target Market(s)

Hip Hop Rap Artist

Colors
3377b5
1b1b1b
33b8a4
919191

Requirements
Must have
• City Skyline clover one of the symbols, GD, Clover, etc.
Nice to have
• dark ominous tone feel, struggle, lone, oneness

```html
<!DOCTYPE html>
<html lang="en">
<head>
<meta charset="utf-8">
<title>GRAVELDUST – Chapters Of A Winter</title>
<link href="https://fonts.googleapis.com/css2?family=Bungee&display=swap" rel="stylesheet">
<style>
  :root {
    --teal-deep: #1f5560;
    --teal: #33707a;
    --teal-bright: #33b8a4;
    --steel-blue: #3377b5;
    --mist: #d6dfe0;
    --mist-warm: #cfc8c2;
    --olive: #b0ab22;
    --lime: #93a836;
    --ink: #1b1b1b;
    --grey: #919191;
    --white: #ffffff;
  }
  * { margin: 0; padding: 0; box-sizing: border-box; }
  html, body {
    width: 1200px;
    height: 1200px;
    overflow: hidden;
    background: var(--ink);
  }
  .album-cover {
    position: relative;
    width: 1200px;
    height: 1200px;
    overflow: hidden;
  }
  .cover-backdrop {
    position: absolute;
    inset: 0;
    background:
      radial-gradient(ellipse 430px 420px at 580px 820px, rgba(225, 232, 232, 0.85), rgba(225, 232, 232, 0) 100%),
      linear-gradient(90deg, rgba(31, 85, 96, 0.95) 0%, rgba(51, 112, 122, 0.55) 18%, rgba(214, 223, 224, 0.05) 45%, rgba(147, 168, 54, 0.45) 75%, rgba(176, 171, 34, 0.95) 100%),
      linear-gradient(180deg, var(--teal) 0%, var(--mist) 60%, var(--mist-warm) 100%);
  }
  .cover-band {
    position: absolute;
    top: 0;
    bottom: 0;
    background: rgba(27, 27, 27, 0.07);
  }
  .cover-band--left { left: 0; width: 165px; }
  .cover-band--right { left: 835px; width: 365px; }
  .skyline {
    position: absolute;
    left: 0;
    bottom: 0;
    width: 1200px;
    height: 420px;
    opacity: 0.38;
  }
  .skyline rect { fill: var(--teal-deep); }
  .cover-figure {
    position: absolute;
    left: 435px;
    top: 495px;
    width: 260px;
    height: 590px;
    border-radius: 110px 110px 40px 40px;
    background: linear-gradient(180deg, rgba(31, 70, 82, 0.92) 0%, rgba(38, 88, 100, 0.85) 60%, rgba(60, 110, 120, 0.35) 100%);
    filter: blur(6px);
  }
  .cover-title {
    position: absolute;
    left: 108px;
    top: 74px;
    width: 984px;
    height: 245px;
  }
  .cover-title text {
    font-family: "Bungee", sans-serif;
    fill: var(--white);
    stroke: var(--ink);
    stroke-width: 6px;
    paint-order: stroke;
  }
  .cover-title .title-shadow { fill: var(--ink); stroke: none; }
  .cover-subtitle {
    position: absolute;
    left: 252px;
    top: 346px;
    width: 704px;
    height: 68px;
  }
  .cover-subtitle text {
    font-family: "Bungee", sans-serif;
    fill: var(--white);
  }
  .clover-mark {
    position: absolute;
    left: 1060px;
    top: 1060px;
    width: 90px;
    height: 90px;
  }
  .clover-mark circle { fill: var(--white); opacity: 0.85; }
  .clover-mark rect { fill: var(--white); opacity: 0.85; }
  .artist-mark {
    position: absolute;
    left: 50px;
    top: 1092px;
    display: flex;
    align-items: center;
    gap: 12px;
    font-family: "Bungee", sans-serif;
    font-size: 34px;
    color: var(--white);
  }
  .artist-mark__dot {
    width: 18px;
    height: 18px;
    border-radius: 50%;
    background: var(--white);
  }
</style>
</head>
<body>
  <main class="album-cover">
    <div class="cover-backdrop" role="img" aria-label="Grainy photograph of a snowstorm washed in teal, white and yellow-green tones"></div>
    <div class="cover-band cover-band--left"></div>
    <div class="cover-band cover-band--right"></div>

    <svg class="skyline" viewBox="0 0 1200 420" aria-hidden="true">
      <rect x="0" y="210" width="70" height="210"/>
      <rect x="75" y="130" width="60" height="290"/>
      <rect x="140" y="240" width="55" height="180"/>
      <rect x="200" y="80" width="45" height="340"/>
      <rect x="212" y="30" width="21" height="60"/>
      <rect x="250" y="190" width="70" height="230"/>
      <rect x="325" y="280" width="60" height="140"/>
      <rect x="810" y="260" width="60" height="160"/>
      <rect x="875" y="150" width="55" height="270"/>
      <rect x="935" y="50" width="60" height="370"/>
      <rect x="955" y="0" width="20" height="60"/>
      <rect x="1000" y="200" width="65" height="220"/>
      <rect x="1070" y="110" width="55" height="310"/>
      <rect x="1130" y="230" width="70" height="190"/>
    </svg>

    <div class="cover-figure" role="img" aria-label="Lone hooded figure seen from behind, walking away into the storm"></div>

    <svg class="cover-title" viewBox="0 0 984 245" aria-label="GRAVELDUST">
      <text class="title-shadow" x="498" y="204" text-anchor="middle" font-size="180" textLength="950" lengthAdjust="spacingAndGlyphs">GRAVELDUST</text>
      <text x="492" y="198" text-anchor="middle" font-size="180" textLength="950" lengthAdjust="spacingAndGlyphs">GRAVELDUST</text>
    </svg>

    <svg class="cover-subtitle" viewBox="0 0 704 68" aria-label="Chapters Of A Winter">
      <text x="352" y="62" text-anchor="middle" font-size="70" textLength="704" lengthAdjust="spacingAndGlyphs">CHAPTERS OF A WINTER</text>
    </svg>

    <svg class="clover-mark" viewBox="0 0 90 90" aria-label="Four-leaf clover">
      <circle cx="32" cy="30" r="15"/>
      <circle cx="58" cy="30" r="15"/>
      <circle cx="32" cy="52" r="15"/>
      <circle cx="58" cy="52" r="15"/>
      <rect x="43" y="58" width="5" height="30"/>
    </svg>

    <div class="artist-mark">
      <span class="artist-mark__dot"></span>
      <span>GD</span>
    </div>
  </main>
</body>
</html>
```